Alaska Personal Injury Lawyer needs a cover for a book

We need a cover for a 90 page paperback book. We want the cover to reflect a positive result coming out of a negative situation.

More specifically, this book discusses the process for maximizing one's personal injury claim arising from automobile accidents.

We are not looking for covers that show pictures of wrecked cars, ambulances or people in wheelchairs. We prefer for the cover to show people who have gotten past their injuries and the legal process and are happy again. Much like many pharmaceutical companies do. They advertise medicines that help horrible conditions, but instead of talking or showing the horrible disease, they show the happy outcome of getting better.

The title of the book with be:
Orchard Under Quiet Hills
Untangling Your Bicycle Mishap Paperwork

I am uploading a book cover on the same topic by someone else who successfully struck a balance between a bad situation and a positive outcome.

It's up to you whether to do an entirely positive cover vs a hybrid such as the one attached. However, the design should communicate more happiness and joy than fear and worry.

Thank you!

people who have been injured in car accidents that were not their fault

Legal

Serif

• We want the cover to reflect a positive result coming out of a negative situation.
• More specifically, this book discusses the process for maximizing one's personal injury claim arising from automobile accidents.
• We prefer for the cover to show people who have gotten past their injuries and the legal process and are happy again. Much like many pharmaceutical companies do. They advertise medicines that help horrible conditions, but instead of talking or showing the horrible disease, they show the happy outcome of getting better or people enjoying life, playing with kids and family.
• It's up to you whether to do an entirely positive cover vs a hybrid such as the one attached. However, the design should communicate more happiness and joy than fear and worry.
• Since the title is "Orchard under Quiet Hills: Untangling Your Bicycle Mishap Paperwork" you might consider a nautical theme, but I encourage you to draw on your own creativity.
• We are not looking for covers that show pictures of wrecked cars, ambulances or people in wheelchairs.
• The title of the book with be:
• Orchard Under Quiet Hills
• Calmly Untangling Your Bicycle Mishap Paperwork
• I am uploading a book cover on the same topic by someone else who successfully struck a balance between a bad situation and a positive outcome.

```html
<!DOCTYPE html>
<html lang="en">
<head>
<meta charset="utf-8">
<title>Orchard Under Quiet Hills — Book Cover</title>
<link href="https://fonts.googleapis.com/css2?family=Arimo:wght@400;700&display=swap" rel="stylesheet">
<style>
  :root {
    --stage-bg: #a3a3a3;
    --cover-top: #f4f4f4;
    --cover-bottom: #dcdcdc;
    --ink-dark: #2e2e2e;
    --accent-red: #a5161b;
    --band-red: #b0151a;
    --band-text: #ffffff;
    --art-light: #8e1b1e;
    --art-dark: #2b2b2b;
  }
  * { margin: 0; padding: 0; box-sizing: border-box; }
  html, body {
    width: 1200px;
    height: 800px;
    overflow: hidden;
  }
  body {
    background: var(--stage-bg);
    font-family: "Arimo", Arial, sans-serif;
    position: relative;
  }
  .book-cover {
    position: absolute;
    left: 345px;
    top: 60px;
    width: 510px;
    height: 680px;
    background: linear-gradient(180deg, var(--cover-top) 0%, var(--cover-bottom) 100%);
    box-shadow: 0 10px 30px rgba(0,0,0,0.25);
    overflow: hidden;
  }
  .cover-art {
    position: absolute;
    left: 120px;
    top: 68px;
    width: 270px;
    height: 258px;
  }
  .title-block {
    position: absolute;
    left: 0;
    top: 345px;
    width: 100%;
    text-align: center;
    text-transform: uppercase;
    font-weight: 700;
  }
  .title-main {
    display: block;
    color: var(--ink-dark);
    font-size: 62px;
    line-height: 60px;
    letter-spacing: -0.03em;
  }
  .title-link {
    display: block;
    color: var(--ink-dark);
    font-size: 24px;
    line-height: 26px;
    letter-spacing: 0;
    margin-top: 2px;
  }
  .title-accent {
    display: block;
    color: var(--accent-red);
    font-size: 84px;
    line-height: 78px;
    letter-spacing: -0.03em;
  }
  .subtitle {
    position: absolute;
    left: 0;
    top: 540px;
    width: 100%;
    text-align: center;
    color: var(--ink-dark);
    font-size: 14px;
    font-weight: 700;
    text-transform: uppercase;
    letter-spacing: 0.01em;
  }
  .author-band {
    position: absolute;
    left: 0;
    top: 592px;
    width: 100%;
    height: 48px;
    background: var(--band-red);
    display: flex;
    align-items: center;
    justify-content: center;
  }
  .author-name {
    color: var(--band-text);
    font-size: 24px;
    font-weight: 400;
    text-transform: uppercase;
    letter-spacing: 0.01em;
  }
</style>
</head>
<body>
  <main class="book-cover">
    <svg class="cover-art" viewBox="0 0 270 258" role="img" aria-label="Illustration of a family of four holding hands beneath a red umbrella">
      <defs>
        <linearGradient id="artTone" x1="0" y1="0" x2="0" y2="1">
          <stop offset="0" stop-color="var(--art-light)"/>
          <stop offset="1" stop-color="var(--art-dark)"/>
        </linearGradient>
      </defs>
      <rect width="270" height="258" fill="url(#artTone)" opacity="0.85"/>
    </svg>

    <h1 class="title-block">
      <span class="title-main">Orchard</span>
      <span class="title-link">Under Quiet</span>
      <span class="title-accent">Hills</span>
    </h1>

    <p class="subtitle">Untangling Your Bicycle Mishap Paperwork</p>

    <div class="author-band">
      <span class="author-name">Martin H. Delacourt</span>
    </div>
  </main>
</body>
</html>
```